Stationary Design Letterhead and Envelope

Artist should provide Letterhead and envelop stationary designs

Info for stationary:
Fernhallow Outdoor Advertising
4873 Quarry Rd. 915 N. PO BOX 528617
Austin, TX 78519

Dale Fernhallow
President
555-862-1907
dale@fernhallowsigns.example
fernhallowsigns.example

Target Market(s)

clients

Colors
0054AA
0677BA
7BADD7
CADEEF
E8F1F8

Requirements
Must have
• high quality unique eye catching and dynamic

```html
<!DOCTYPE html>
<html lang="en">
<head>
<meta charset="utf-8">
<title>Fernhallow Outdoor Advertising – Stationery</title>
<link href="https://fonts.googleapis.com/css2?family=Roboto:wght@400;500;700&display=swap" rel="stylesheet">
<style>
  :root{
    --navy:#0054AA;
    --blue:#0677BA;
    --sky:#7BADD7;
    --mist:#CADEEF;
    --ice:#E8F1F8;
    --ink:#1c1f24;
    --grey:#6b6f76;
    --paper:#ffffff;
    --backdrop:#ece6da;
  }
  *{box-sizing:border-box;margin:0;padding:0}
  html,body{width:1200px;height:783px;overflow:hidden}
  body{background:var(--backdrop);font-family:"Roboto",sans-serif;color:var(--ink);position:relative}

  .sheet{position:absolute;background:var(--paper);overflow:hidden;box-shadow:0 6px 18px rgba(60,50,30,.18)}
  .letterhead{left:60px;top:40px;width:490px;height:703px}
  .envelope-front{left:600px;top:100px;width:560px;height:245px}
  .envelope-back{left:600px;top:395px;width:560px;height:245px}

  .art{position:absolute;left:0;top:0;width:100%;height:100%}

  .brand{position:absolute;color:var(--navy);font-weight:700;line-height:1}
  .brand-name{display:block;letter-spacing:.5px;text-transform:uppercase}
  .brand-tag{display:block;text-transform:uppercase;letter-spacing:.6px;margin-top:3px}

  .letterhead .brand{left:42px;top:48px}
  .letterhead .brand-name{font-size:19px}
  .letterhead .brand-tag{font-size:6.5px}

  .date{position:absolute;right:60px;top:170px;font-size:7.5px;color:var(--grey)}

  .sender{position:absolute;left:62px;top:198px;font-size:7px;line-height:1.55;color:var(--grey)}
  .sender-name{font-size:11px;font-weight:700;color:var(--ink)}
  .sender-name span{color:var(--blue)}
  .sender b{color:var(--blue)}

  .body-copy{position:absolute;left:62px;right:48px;top:290px;font-size:9px;line-height:1.8;color:var(--grey);text-align:justify}
  .body-copy p{margin-bottom:12px}

  .seal{position:absolute;left:360px;top:510px;width:58px;height:58px;border-radius:50%;border:2px solid var(--sky);opacity:.6}

  .contacts{position:absolute;list-style:none;display:grid;grid-auto-flow:column;grid-template-rows:repeat(2,auto);column-gap:22px;row-gap:6px;font-size:7.5px;color:var(--ink)}
  .contact{display:flex;align-items:center;gap:6px;white-space:nowrap}
  .icon{width:11px;height:11px;flex:none}
  .letterhead .contacts{left:60px;top:612px}
  .envelope-front .contacts{left:20px;top:184px;font-size:7px;column-gap:16px;row-gap:7px}

  .envelope-front .brand{left:34px;top:20px}
  .envelope-front .brand-name{font-size:16px}
  .envelope-front .brand-tag{font-size:5.5px}

  .envelope-back .brand{right:16px;bottom:16px;text-align:right}
  .envelope-back .brand-name{font-size:11px}
  .envelope-back .brand-tag{font-size:4.2px;margin-top:2px}
</style>
</head>
<body>

<!-- Letterhead -->
<section class="sheet letterhead" aria-label="Letterhead">
  <svg class="art" viewBox="0 0 490 703" aria-hidden="true">
    <!-- header: soft band with stacked bars -->
    <rect x="0" y="0" width="490" height="8" fill="var(--navy)"/>
    <rect x="260" y="8" width="230" height="102" fill="var(--ice)"/>
    <rect x="300" y="34" width="190" height="10" fill="var(--sky)"/>
    <rect x="340" y="52" width="150" height="10" fill="var(--blue)"/>
    <rect x="380" y="70" width="110" height="10" fill="var(--mist)"/>
    <line x1="42" y1="94" x2="240" y2="94" stroke="var(--mist)" stroke-width="1"/>
    <!-- footer: plain stacked bands -->
    <line x1="0" y1="660" x2="490" y2="660" stroke="var(--mist)" stroke-width="1"/>
    <rect x="0" y="676" width="490" height="27" fill="var(--ice)"/>
    <rect x="0" y="676" width="180" height="6" fill="var(--sky)"/>
    <rect x="0" y="695" width="490" height="8" fill="var(--navy)"/>
  </svg>

  <div class="brand">
    <span class="brand-name">Fernhallow</span>
    <span class="brand-tag">Outdoor Advertising</span>
  </div>

  <p class="date">Date : 13 April, 2022</p>

  <div class="sender">
    <p class="sender-name">Dale <span>Fernhallow</span></p>
    <p>President</p>
    <p><b>A :</b> PO BOX 528617 Austin, TX 78519</p>
    <p><b>W :</b> fernhallowsigns.example</p>
    <p><b>P :</b> +555 862 1907</p>
  </div>

  <div class="body-copy">
    <p>Lorem ipsum dolor sit amet, consectetur adipisicing elit, sed do eiusmod tempor incididunt ut labore et dolore magna aliqua. Ut enim ad minim veniam, quis nostrud exercitation ullamco laboris nisi ut aliquip ex ea commodo consequat.</p>
    <p>Excepteur sint occaecat cupidatat non proident, sunt in culpa qui officia deserunt mollit anim id est laborum. Sed ut perspiciatis unde omnis iste natus error sit voluptatem accusantium doloremque laudantium, totam rem aperiam, eaque ipsa quae ab illo inventore veritatis et quasi architecto beatae vitae dicta sunt explicabo. Nemo enim ipsam voluptatem quia voluptas sit aspernatur aut odit aut fugit, sed quia voluptatem sequi nesciunt.</p>
    <p>Neque porro quisquam dolorem ipsum quia dolor sit amet, consectetur magnam aliquam quaerat voluptatem. Sunt in culpa qui officia iste natus error sit voluptatem doloremque laudantium.</p>
  </div>

  <div class="seal" role="img" aria-label="Company stamp"></div>

  <ul class="contacts">
    <li class="contact"><svg class="icon" viewBox="0 0 12 12"><circle cx="6" cy="6" r="6" fill="var(--blue)"/><rect x="4.2" y="2.6" width="3.6" height="6.8" rx=".8" fill="#fff"/></svg>+555 862 1907</li>
    <li class="contact"><svg class="icon" viewBox="0 0 12 12"><circle cx="6" cy="6" r="6" fill="var(--blue)"/><circle cx="6" cy="6" r="3" fill="none" stroke="#fff" stroke-width=".9"/><line x1="3" y1="6" x2="9" y2="6" stroke="#fff" stroke-width=".8"/></svg>fernhallowsigns.example</li>
    <li class="contact"><svg class="icon" viewBox="0 0 12 12"><circle cx="6" cy="6" r="6" fill="var(--blue)"/><rect x="3" y="4" width="6" height="4.2" fill="none" stroke="#fff" stroke-width=".9"/><polyline points="3,4 6,6.4 9,4" fill="none" stroke="#fff" stroke-width=".8"/></svg>dale@fernhallowsigns.example</li>
    <li class="contact"><svg class="icon" viewBox="0 0 12 12"><circle cx="6" cy="6" r="6" fill="var(--blue)"/><path d="M6 2.6a2.2 2.2 0 0 1 2.2 2.2C8.2 6.4 6 9.4 6 9.4S3.8 6.4 3.8 4.8A2.2 2.2 0 0 1 6 2.6z" fill="#fff"/></svg>4873 Quarry Rd. 915 N. PO BOX 528617 Austin, TX 78519.</li>
  </ul>
</section>

<!-- Envelope front -->
<section class="sheet envelope-front" aria-label="Envelope front">
  <svg class="art" viewBox="0 0 560 245" aria-hidden="true">
    <rect x="0" y="0" width="560" height="6" fill="var(--navy)"/>
    <rect x="330" y="6" width="230" height="84" fill="var(--ice)"/>
    <rect x="370" y="26" width="190" height="9" fill="var(--sky)"/>
    <rect x="410" y="42" width="150" height="9" fill="var(--blue)"/>
    <rect x="450" y="58" width="110" height="9" fill="var(--mist)"/>
    <rect x="0" y="237" width="560" height="8" fill="var(--ice)"/>
  </svg>

  <div class="brand">
    <span class="brand-name">Fernhallow</span>
    <span class="brand-tag">Outdoor Advertising</span>
  </div>

  <ul class="contacts">
    <li class="contact"><svg class="icon" viewBox="0 0 12 12"><rect width="12" height="12" rx="2" fill="var(--blue)"/><rect x="4.2" y="2.4" width="3.6" height="7.2" rx=".8" fill="#fff"/></svg>+555 862 1907</li>
    <li class="contact"><svg class="icon" viewBox="0 0 12 12"><rect width="12" height="12" rx="2" fill="var(--blue)"/><rect x="3" y="4" width="6" height="4.2" fill="none" stroke="#fff" stroke-width=".9"/><polyline points="3,4 6,6.4 9,4" fill="none" stroke="#fff" stroke-width=".8"/></svg>dale@fernhallowsigns.example</li>
    <li class="contact"><svg class="icon" viewBox="0 0 12 12"><rect width="12" height="12" rx="2" fill="var(--blue)"/><circle cx="6" cy="6" r="3" fill="none" stroke="#fff" stroke-width=".9"/><line x1="3" y1="6" x2="9" y2="6" stroke="#fff" stroke-width=".8"/></svg>fernhallowsigns.example</li>
    <li class="contact"><svg class="icon" viewBox="0 0 12 12"><rect width="12" height="12" rx="2" fill="var(--blue)"/><path d="M6 2.4a2.2 2.2 0 0 1 2.2 2.2C8.2 6.2 6 9.4 6 9.4S3.8 6.2 3.8 4.6A2.2 2.2 0 0 1 6 2.4z" fill="#fff"/></svg>4873 Quarry Rd. 915 N. PO BOX 528617 Austin, TX 78519.</li>
  </ul>
</section>

<!-- Envelope back -->
<section class="sheet envelope-back" aria-label="Envelope back">
  <svg class="art" viewBox="0 0 560 245" aria-hidden="true">
    <path d="M0,0 H560 L540,80 Q532,100 510,100 H50 Q28,100 20,80 Z" fill="var(--ice)"/>
  </svg>
  <div class="brand">
    <span class="brand-name">Fernhallow</span>
    <span class="brand-tag">Outdoor Advertising</span>
  </div>
</section>

</body>
</html>
```